Web Design Project

I'm looking for a major redesign for my existing photographic art website: www.brightmeadowframes.com. Here are my complaints about the current layout: 1) It looks unsophisticated (we will, of course, delete the "sale" banner; 2) the images are vastly too small when displayed in the gallery; 3) I'm not wild about the navigation; 4) the Flash has got to go; 4) there has to be an easy way to significantly enlarge the photos for viewing; 5) the copy is a bit over the top - we will be rewriting it. Other than that, it's a good site :)

The market for the photography is principally commercial applications - interior designers, etc. who are concerned with how these images will look in hospitals, office buildings, etc. The leading competitor in this space has a much better site: www.walterpikens.com. Another site worth viewing is: www.morvelt.com. This site is much more akin to my site.

We will be reducing the number of photos available. Total count will be approximately 400. The largest collection will be the "digital garden" - close up photography of flowers, plants, etc.
Updates

I am amazed at the quality of the submissions - which has made the selection process very, very difficult. Each of you should be very proud of the quality of work you produce. Beyond this web-site, which is a "sideline" for me, I run a large marketing organization....and have shared these submissions with all of my colleagues who were duly impressed. Hopefully we will have an opportunity to work with you on a differentp project!

Thank you!!!
Peter

Industry/Entity Type

Digital

```html
<!DOCTYPE html>
<html lang="en">
<head>
<meta charset="utf-8">
<title>Bright Meadow — Gallery</title>
<link href="https://fonts.googleapis.com/css2?family=Vollkorn:wght@400;600&family=Arimo:wght@400;700&display=swap" rel="stylesheet">
<style>
  :root {
    --wood-dark: #141210;
    --wood-mid: #2a2622;
    --panel: #4a4845;
    --panel-light: #5a5855;
    --rule: #0c0b0a;
    --rule-light: #3c3934;
    --text-light: #f2f2f2;
    --text-muted: #a9a6a0;
    --footer-text: #7a7671;
    --accent-red: #d8141b;
    --button-red: #8e0d0d;
    --sale-yellow: #f2ea1e;
    --white: #ffffff;
  }
  * { margin: 0; padding: 0; box-sizing: border-box; }
  html, body { width: 1200px; height: 980px; overflow: hidden; }
  body {
    position: relative;
    background:
      radial-gradient(ellipse at 50% 45%, rgba(70,64,58,0.35), rgba(0,0,0,0) 65%),
      repeating-linear-gradient(90deg, rgba(255,255,255,0.025) 0 2px, rgba(0,0,0,0.05) 2px 7px, rgba(255,255,255,0.015) 7px 11px),
      linear-gradient(180deg, var(--wood-mid), var(--wood-dark));
    font-family: "Arimo", Arial, sans-serif;
    color: var(--text-light);
  }
  .auth-button {
    position: absolute; top: 12px; height: 28px; width: 70px;
    background: linear-gradient(180deg, #a51414, var(--button-red));
    border-radius: 3px; color: #f0d0d0;
    font-size: 12px; line-height: 28px; text-align: center;
  }
  .auth-login { left: 932px; }
  .auth-signup { left: 1008px; }

  .photo-search {
    position: absolute; left: 130px; top: 86px; width: 185px; height: 28px;
    background: linear-gradient(180deg, #727170, #5a5958);
    border-radius: 3px; font-size: 13px; color: #e4e4e4;
    line-height: 28px; padding-left: 14px;
  }
  .photo-search-button {
    position: absolute; right: 0; top: 0; width: 34px; height: 28px;
    border-left: 1px solid #3e3d3c; background: #6a6968; border-radius: 0 3px 3px 0;
  }
  .photo-search-button svg { position: absolute; left: 8px; top: 5px; }

  .brand {
    position: absolute; left: 400px; top: 88px; width: 406px; text-align: center;
    font-family: "Vollkorn", Georgia, serif; font-size: 25px; color: var(--text-light);
    letter-spacing: 0.5px;
  }

  .cart-status {
    position: absolute; right: 122px; top: 100px; font-size: 12px; color: var(--text-muted);
    display: flex; align-items: center; gap: 6px;
  }

  .main-nav {
    position: absolute; left: 130px; top: 145px; width: 948px; height: 51px;
    border-top: 1px solid var(--rule); border-bottom: 1px solid var(--rule);
    box-shadow: 0 1px 0 var(--rule-light), inset 0 1px 0 var(--rule-light);
  }
  .main-nav a {
    position: absolute; top: 17px; font-family: "Vollkorn", Georgia, serif;
    font-size: 14px; color: var(--text-light); text-decoration: none; letter-spacing: 0.3px;
  }
  .main-nav a.is-active { color: var(--accent-red); }

  .sale-banner {
    position: absolute; left: 130px; top: 224px; width: 948px; height: 73px;
    background: linear-gradient(180deg, var(--panel-light), var(--panel));
    text-align: center; border-bottom: 2px solid #2a2927;
  }
  .sale-banner h2 {
    font-family: "Vollkorn", Georgia, serif; font-weight: 400; font-size: 23px;
    color: var(--sale-yellow); margin-top: 8px;
  }
  .sale-banner p { font-family: "Vollkorn", Georgia, serif; font-size: 14.5px; margin-top: 2px; }

  .feature-frame {
    position: absolute; left: 130px; top: 298px; width: 948px; height: 421px; background: var(--white);
  }
  .feature-photo {
    position: absolute; left: 15px; top: 15px; width: 919px; height: 391px;
    background:
      linear-gradient(180deg, #0b0f12 0%, #101418 40%, #2b3238 62%, #1f4fd0 72%, #0aa3e0 80%, #0c1a22 90%, #07090b 100%);
  }

  .info-band {
    position: absolute; left: 130px; top: 719px; width: 948px; height: 141px;
    background: linear-gradient(180deg, var(--panel), #55534f);
  }
  .info-band h3 {
    position: absolute; font-family: "Vollkorn", Georgia, serif; font-weight: 400;
    font-size: 23px; color: var(--text-muted);
  }
  .contact-heading { left: 35px; top: 15px; }
  .contact-phone { position: absolute; left: 37px; top: 56px; font-size: 14px; font-weight: 700; }
  .info-divider { position: absolute; left: 250px; top: 40px; width: 1px; height: 75px; background: #3a3936; }
  .welcome-heading { left: 282px; top: 16px; }
  .welcome-copy {
    position: absolute; left: 284px; top: 56px; width: 640px;
    font-size: 11.8px; line-height: 17.5px; color: var(--text-light);
  }

  .footer-links {
    position: absolute; left: 130px; top: 880px; font-size: 12px; color: var(--footer-text);
  }
  .footer-links span.sep { margin: 0 7px; }
  .copyright {
    position: absolute; right: 122px; top: 882px; font-size: 12px; color: var(--footer-text);
  }
</style>
</head>
<body>
  <header>
    <a class="auth-button auth-login">Login</a>
    <a class="auth-button auth-signup">Sign Up</a>

    <div class="photo-search">Find a Photo
      <span class="photo-search-button">
        <svg width="18" height="18" viewBox="0 0 18 18"><circle cx="7" cy="7" r="5" fill="none" stroke="#f2f2f2" stroke-width="2"/><line x1="11" y1="11" x2="16" y2="16" stroke="#f2f2f2" stroke-width="3" stroke-linecap="round"/></svg>
      </span>
    </div>

    <div class="brand">Bright Meadow</div>

    <div class="cart-status">You have 0 items in your cart
      <svg width="28" height="20" viewBox="0 0 28 20"><path d="M1 2h5l3 11h14l3-8H8" fill="none" stroke="#b02020" stroke-width="2"/><circle cx="11" cy="17" r="2" fill="#8a8680"/><circle cx="21" cy="17" r="2" fill="#8a8680"/></svg>
    </div>

    <nav class="main-nav">
      <a class="is-active" style="left:64px">GALLERY</a>
      <a style="left:170px">ARCHITECTS / DESIGNERS</a>
      <a style="left:401px">ABOUT THE ARTIST</a>
      <a style="left:589px">ORDERING INFORMATION</a>
      <a style="left:816px">CONTACT US</a>
    </nav>
  </header>

  <main>
    <section class="sale-banner">
      <h2>SALE! All photographs 30% off.</h2>
      <p>Discount will be applied automatically in the shopping cart as part of the ordering process.</p>
    </section>

    <section class="feature-frame">
      <div class="feature-photo" role="img" aria-label="Night city skyline over a river with a bridge lit in bright blue"></div>
    </section>

    <section class="info-band">
      <h3 class="contact-heading">Get in touch</h3>
      <p class="contact-phone">Phone : 877- 555 - 0142</p>
      <div class="info-divider"></div>
      <h3 class="welcome-heading">Bright Meadow welcome for you</h3>
      <p class="welcome-copy">Welcome to the world of Peter Halvorsen. Come in and enjoy a place where stunning horizons meet glorious skies. A place where light and shade dance together in flawless rhythm. Come in and discover a world of photography that begins and ends with a shutter. Come in, relax and browse the gallery. You are about to experience some of the most inspiring and enchanting imagery the world has to offer.</p>
    </section>
  </main>

  <footer>
    <div class="footer-links">Gallery<span class="sep">|</span>Architects/Designers<span class="sep">|</span>About the Artist<span class="sep">|</span>Ordering Information<span class="sep">|</span>Contact Us</div>
    <div class="copyright">© 2010 Halvorsen Photography</div>
  </footer>
</body>
</html>
```